Best Seller Cover Design for Inspirational Non-Fiction, Self-Help Book

I've been working diligently on a book title "Quiet Harbor Ascent" that will be pivotal for my coaching business. We're heavily investing in marketing and public relations for this and would love it to be a best seller (every other's dream). I need an amazing book cover design that is eye-catching, description, creative, interesting, and compelling, Can you work your magic?I've attached a detailed description along with the content for the back cover. Please let me know if all the content does not fit and I'm happy to reduce it. I need a cover that sells and speaks to the description, whatever you think that will be best. Book DetailsTitle: Self-Defined SuccessSubtitle: Spoiler Alert: You Already Have Everything It TakesAuthor: Ngan H. NguyenSpecifics:- The book will be 5.5" by 8.5" and 216 pages (may change slightly and we can update the spine in final revisions). - Paperback and leave space for a bar code- Will need the raw files so this can be redesigned into hardcover down the line- Brindlecart book cover upload ready- Final file will also need the front cover only for e-book version- Add profile headshot (attached) to back-cover if space permits.I do not have a clear vision of what will be best for this cover but I really like the evocative style of Warren Kestoly Plenitude book. Thank you!

Target Market(s)

Professionals in transition, aspiring or new entrepreneurs, change-makers.

Font styles to use
Serif
Script

Colors

Designer to choose colors to be used in the design.

Requirements
Must have
• Traditional but with elements that make it interesting and provocative since it is speaking to a twist on a topic that has been well talked about, success.

```html
<!DOCTYPE html>
<html lang="en">
<head>
<meta charset="utf-8">
<title>Quiet Harbor Ascent — Book Cover</title>
<link rel="stylesheet" href="https://fonts.googleapis.com/css2?family=Oswald:wght@600;700&family=Montserrat:wght@800&family=Crimson+Text:wght@400;700&family=Questrial&display=swap">
<style>
  :root {
    --page-bg: #e9e8e6;
    --cover-grey: #b3acae;
    --cover-grey-light: #bdb7b9;
    --spine-grey: #aaa3a5;
    --accent-yellow: #fcc800;
    --text-white: #fbfafa;
    --text-black: #141210;
    --photo-warm: #d9b38a;
    --photo-grey: #c4c0c2;
  }
  * { box-sizing: border-box; margin: 0; padding: 0; }
  html, body { width: 1200px; height: 800px; overflow: hidden; }
  body { background: var(--page-bg); }

  .book-wrap {
    position: absolute; left: 117px; top: 50px;
    width: 966px; height: 700px;
    display: flex;
    box-shadow: 0 10px 30px rgba(0,0,0,.18);
  }

  /* Back cover */
  .back-cover {
    width: 453px; height: 700px;
    background: var(--cover-grey);
    padding: 46px 38px 0 38px;
    color: var(--text-white);
    font-family: "Questrial", sans-serif;
    position: relative;
  }
  .back-tagline {
    color: var(--accent-yellow);
    font-size: 11.5px;
    text-align: center;
    margin-bottom: 12px;
  }
  .back-blurb p {
    font-size: 12px;
    line-height: 1.45;
    text-align: justify;
    margin-bottom: 10px;
  }
  .author-bio { margin-top: 18px; overflow: hidden; }
  .author-photo {
    float: left;
    width: 106px; height: 120px;
    margin: 2px 10px 4px 0;
    background: linear-gradient(160deg, #44505a, #2a2320 70%, #1a1716);
  }
  .author-bio p { font-size: 12px; line-height: 1.45; text-align: justify; }
  .author-bio .author-name { color: var(--accent-yellow); font-style: normal; font-weight: 400; }

  /* Spine */
  .spine {
    width: 60px; height: 700px;
    background: var(--spine-grey);
    border-left: 1px solid rgba(0,0,0,.08);
    border-right: 1px solid rgba(0,0,0,.08);
    display: flex; align-items: center; justify-content: flex-start;
    writing-mode: vertical-rl;
    padding-top: 60px;
    gap: 42px;
  }
  .spine-title {
    font-family: "Montserrat", sans-serif; font-weight: 800;
    color: var(--accent-yellow); font-size: 21px; letter-spacing: 2px;
  }
  .spine-author {
    font-family: "Questrial", sans-serif;
    color: var(--text-white); font-size: 17px; letter-spacing: 3px;
  }

  /* Front cover */
  .front-cover {
    width: 453px; height: 700px;
    background: linear-gradient(180deg, var(--cover-grey) 0%, var(--cover-grey-light) 60%, var(--cover-grey) 100%);
    position: relative;
    text-align: center;
  }
  .front-title {
    color: var(--accent-yellow);
    padding-top: 50px;
    line-height: .95;
  }
  .front-title .title-line-1 {
    display: block;
    font-family: "Oswald", sans-serif; font-weight: 700;
    font-size: 52px; letter-spacing: .5px;
  }
  .front-title .title-line-2 {
    display: block;
    font-family: "Montserrat", sans-serif; font-weight: 800;
    font-size: 68px; letter-spacing: 1px;
  }
  .subtitle {
    margin: 22px auto 0; width: 312px;
    border-top: 1.5px solid var(--accent-yellow);
    border-bottom: 1.5px solid var(--accent-yellow);
    padding: 8px 0 10px;
    font-family: "Crimson Text", serif;
    color: var(--text-white);
    font-size: 18px; line-height: 1.35;
  }
  .cover-image {
    position: absolute; left: 30px; top: 345px;
    width: 393px; height: 285px;
    background:
      radial-gradient(ellipse 70px 110px at 50% 42%, var(--photo-warm), rgba(217,179,138,0) 100%),
      radial-gradient(ellipse at 50% 50%, #cfcacc, var(--photo-grey) 80%);
    opacity: .95;
  }
  .author-band {
    position: absolute; left: 0; bottom: 0;
    width: 100%; height: 70px;
    background: var(--accent-yellow);
    display: flex; align-items: center; justify-content: center;
    font-family: "Crimson Text", serif; font-weight: 700;
    color: var(--text-black); font-size: 30px; letter-spacing: .5px;
  }
</style>
</head>
<body>
  <main class="book-wrap">
    <section class="back-cover">
      <p class="back-tagline">When all is said and done, what will matter to you most?</p>
      <div class="back-blurb">
        <p>Following someone else’s path or society’s definition of “success” doesn’t often lead to personal fulfillment. At the end of the day, we genuinely want to succeed—not live a life defined by others.</p>
        <p>You can achieve anything you desire, and when you aim high for your spark of passion you will succeed. Passion is what awakens the heart, fires the soul, and fills the spirit. It is passion that energizes and sparks the pull forward through all barriers, uncertainty, and challenges.</p>
        <p>On this journey, we are asked to turn inward and search for the invisible, the hidden, and the sacred possibilities in order to claim what is ours in truth. We will then fill that shell with a desire that will ignite its creation.</p>
        <p>May this book serve as your guide on how to evoke this clarity and desire for your most authentic path enabling you to create a vision for your future that will bring you the ultimate sense of fulfillment. In addition, this book will show you the steps to navigate the path forward toward this new dream giving you the opportunity to awaken innate abilities you didn’t know you had that will open the door to success.</p>
      </div>
      <div class="author-bio">
        <div class="author-photo" role="img" aria-label="Author headshot photograph"></div>
        <p><em class="author-name">Thira M.Olsberg</em> has built her platform of a vision-driven life after 10 years of experience working as a business strategy advisor in Meridian 500 companies and at Harrowgate &amp; Partners. Combining her advisory experience with her passion for spiritual principles of success, she now empowers entrepreneurs, change-makers, and leaders to step into their truth and bring their unique vision to life. Enabling them to change their lives, revolutionize their work, create greater impact in the world.</p>
      </div>
    </section>

    <section class="spine">
      <span class="spine-title">QUIET HARBOR ASCENT</span>
      <span class="spine-author">THIRA M.OLSBERG</span>
    </section>

    <section class="front-cover">
      <h1 class="front-title">
        <span class="title-line-1">QUIET HARBOR</span>
        <span class="title-line-2">ASCENT</span>
      </h1>
      <p class="subtitle">Plot Reveal: The Compass Was Yours<br>From the Start</p>
      <div class="cover-image" role="img" aria-label="Glowing vintage light bulb surrounded by hand-sketched business diagrams and charts"></div>
      <div class="author-band">THIRA M.OLSBERG</div>
    </section>
  </main>
</body>
</html>
```